Wordpress template for a mens-choire webpage

Task is to design a Wordpress template for an 98 years old estonian mens choire webpage.
Design should involve details from the attached files, choire logo and the colors of the choire flag: in horizontal orientation bright sky-blue, white, bright grass-green.
Designer signature is allowed to be added to the template, with country of origin.

Thank you everyone for your great designs!
Our project has now entered into a voting and decision phase until 14th of March 2014 (included).

```html
<!DOCTYPE html>
<html lang="en">
<head>
<meta charset="utf-8">
<title>Lindvale Men's Choir</title>
<link rel="stylesheet" href="https://fonts.googleapis.com/css2?family=Arimo&family=Cabin:wght@400;500&family=Molengo&display=swap">
<style>
  :root {
    --page-bg: #e3e3e3;
    --sheet: #ffffff;
    --sky: #1ccbf1;
    --sky-deep: #1c9ff0;
    --grass: #3d9e3c;
    --grass-bright: #56c22e;
    --panel: #f2f2f2;
    --text: #8a8a8a;
    --link: #17a9d8;
    --photo-top: #f2f2f2;
    --photo-mid: #2c2c33;
    --keys-dark: #2a2a2a;
    --keys-light: #d8d8d8;
  }
  * { box-sizing: border-box; margin: 0; padding: 0; }
  html, body { width: 1039px; height: 1200px; overflow: hidden; }
  body { background: var(--page-bg); font-family: "Cabin", sans-serif; color: var(--text); position: relative; }
  .sheet { position: absolute; left: 78px; top: 8px; width: 886px; height: 1125px; background: var(--sheet); }
  .hero { position: absolute; left: 8px; top: 6px; width: 870px; height: 270px;
    background: linear-gradient(180deg, var(--photo-top) 0%, var(--photo-top) 14%, var(--photo-mid) 48%, #1d1d22 100%);
    display: flex; align-items: flex-end; justify-content: center; padding-bottom: 18px; }
  .hero-name { font-family: "Cabin", sans-serif; font-size: 16px; color: #ffffff; letter-spacing: 1px; display: flex; align-items: center; gap: 8px; }
  .hero-name .dot { width: 14px; height: 14px; border-radius: 50%; background: #ffffff; }
  .nav { position: absolute; left: 0; top: 283px; width: 886px; height: 62px; background: var(--sky); display: flex; list-style: none; }
  .nav li { height: 62px; display: flex; align-items: center; justify-content: center; font-family: "Molengo", sans-serif; font-size: 18px; color: #ffffff; }
  .nav .home { width: 102px; box-shadow: inset 0 3px 0 var(--sky-deep); }
  .nav .about { width: 132px; }
  .nav .contact { width: 116px; background: var(--sky-deep); }
  .nav .page4 { width: 98px; }
  .panel-title { background: var(--panel); border-radius: 6px; height: 51px; display: flex; align-items: center; padding-left: 9px;
    font-family: "Arimo", sans-serif; font-size: 18px; font-weight: 400; color: var(--grass); }
  .welcome { position: absolute; left: 19px; top: 363px; width: 842px; }
  .body-text { font-size: 11.2px; line-height: 14.2px; margin-top: 12px; }
  .more { color: var(--link); font-weight: 500; font-size: 12px; letter-spacing: .3px; }
  .posts { position: absolute; left: 19px; top: 546px; display: flex; gap: 29px; }
  .post { width: 262px; }
  .post.latest .panel-title { color: var(--grass-bright); }
  .keys { width: 139px; height: 139px; margin-top: 10px; background: linear-gradient(160deg, var(--keys-dark) 0%, var(--keys-dark) 38%, #7a7a7a 55%, var(--keys-light) 75%, #f4f4f4 100%); }
  .post.wrap .keys { float: left; margin-right: 8px; }
  .post .body-text { margin-top: 10px; }
  .post .more { display: inline-block; margin-top: 4px; }
  .footer { position: absolute; left: 5px; top: 1031px; width: 875px; height: 91px; background: var(--sky); }
  .social { position: absolute; left: 19px; top: 15px; display: flex; gap: 11px; list-style: none; }
  .social li { width: 31px; height: 31px; border-radius: 5px; }
  .social .s1 { background: #3a5a98; }
  .social .s2 { background: #2aa6c7; }
  .social .s3 { background: #ef8a26; }
  .legal { position: absolute; left: 0; right: 0; top: 38px; text-align: center; color: #ffffff; font-size: 9px; line-height: 18px; font-weight: 500; }
</style>
</head>
<body>
  <div class="sheet">
    <div class="hero" role="img" aria-label="Group photo of the choir members in dark suits with the choir emblem in front">
      <span class="hero-name"><span class="dot"></span>Lindvale Men's Choir</span>
    </div>

    <ul class="nav">
      <li class="home">Home</li>
      <li class="about">About Us</li>
      <li class="contact">Contact</li>
      <li class="page4">Page 4</li>
    </ul>

    <section class="welcome">
      <h1 class="panel-title">Welcome to our site</h1>
      <p class="body-text">Hello, We are 98 years old estonian mens choire. Lorem ipsum dolor sit amet, consectetur adipiscing elit. Ut eu turpis metus. Vivamus fermentum dapibus lorem, non mollis lorem egestas non. Nulla blandit erat placerat, porta ipsum in, fermentum nulla. Maecenas congue tempus tincidunt. Morbi condimentum, ante id laoreet rutrum, eros risus viverra orci, quis volutpat elit nisl ut lacus. Aliquam erat mauris, ornare id leo nec, hendrerit venenatis tortor. Curabitur pellentesque dolor vitae imperdiet mattis. In eu vestibulum lacus, eu venenatis est. Proin porta ultrices eros, eu placerat nunc convallis mollis. Donec a metus suscipit sem dapibus vehicula at quis mauris. Suspendisse iaculis risus nec tortor aliquet, sed pellentesque neque fringilla. Pellentesque tempor non ligula at lacinia. <span class="more">Continue reading &rarr;</span></p>
    </section>

    <div class="posts">
      <article class="post wrap">
        <h2 class="panel-title">Test post 2</h2>
        <div class="keys" role="img" aria-label="Close-up photo of piano keys"></div>
        <p class="body-text">Morbi ligula ante, gravida nec turpis sit amet, viverra auctor dolor. Ut rutrum sed magna vel euismod. Ut et auctor felis. Cras ullamcorper, arcu id feugiat tincidunt, metus sem facilisis justo, id laoreet metus metus in quam. Vestibulum adipiscing lacus id ultrices pharetra. Nunc cursus neque commodo enim accumsan egestas. Nullam vestibulum bibendum tincidunt. Maecenas id augue risus. Aliquam ultrices odio in tortor gravida sagittis sed sed sapien. Maecenas bibendum purus quis enim scelerisque, lacinia fringilla nunc cursus. Curabitur sit amet consequat justo, condimentum varius dui. <span class="more">Continue reading &rarr;</span></p>
      </article>
      <article class="post">
        <h2 class="panel-title">Test post 1</h2>
        <div class="keys" role="img" aria-label="Close-up photo of piano keys"></div>
        <p class="body-text">Lorem ipsum dolor sit amet, consectetur adipiscing elit. Ut eu turpis metus. Vivamus fermentum dapibus lorem, non mollis lorem egestas non. Nulla blandit erat placerat, porta ipsum in, fermentum nulla. Maecenas congue tempus tincidunt. Morbi condimentum, ante id laoreet rutrum, eros risus viverra orci, quis volutpat elit nisl ut lacus. Aliquam erat mauris, ornare id leo nec, hendrerit venenatis tortor. Curabitur pellentesque dolor vitae imperdiet mattis. In eu vestibulum lacus, eu venenatis est. Proin porta ultrices eros, eu placerat nunc convallis mollis. Donec a metus suscipit sem dapibus mauris.</p>
        <span class="more">Continue reading &rarr;</span>
      </article>
      <article class="post latest">
        <h2 class="panel-title">Headline</h2>
        <div class="keys" role="img" aria-label="Close-up photo of piano keys"></div>
        <p class="body-text">Morbi ligula ante, gravida nec turpis sit amet, viverra auctor dolor. Ut rutrum sed magna vel euismod. Ut et auctor felis. Cras ullamcorper, arcu id feugiat tincidunt, metus sem facilisis justo, id laoreet metus metus in quam. Vestibulum adipiscing lacus id ultrices pharetra. Nunc cursus neque commodo enim accumsan egestas. Nullam vestibulum bibendum tincidunt. Maecenas id augue risus. Aliquam ultrices odio in tortor gravida sagittis sed sed sapien. Maecenas bibendum purus quis enim scelerisque, lacinia fringilla nunc cursus. Curabitur sit amet consequat justo, condimentum varius dui. <span class="more">Continue reading &rarr;</span></p>
      </article>
    </div>

    <footer class="footer">
      <ul class="social">
        <li class="s1"></li>
        <li class="s2"></li>
        <li class="s3"></li>
      </ul>
      <p class="legal">2014<br>Copyright@Example.com</p>
    </footer>
  </div>
</body>
</html>
```